We are an integrated facilities management company.

We aggregate everything related to facilities maintenance. Repair-replacement of equipment and facility space materials from:
Asset gathering and tracking.
Vendor screening, contracting and management.
Service requirement development.
Work order processing and management.
Invoice reconciliation.
Vendor payment.
Reporting.
Capital equipment bids and project management.

Target Market(s)

Retail, hospitality, multi-family housing, long term healthcare.

Industry/Entity Type

Maintenance

Contact Information for Business Card

Professional and bold look. (see logo zip file)

Colors
3377b5
85abd2
cedeed

Requirements
Must have
• N/A
Nice to have
• N/A
Should not have
• N/A

```html
<!DOCTYPE html>
<html lang="en">
<head>
<meta charset="utf-8">
<title>Keystone Facility Services – Business Card</title>
<link rel="stylesheet" href="https://fonts.googleapis.com/css2?family=Poppins:wght@400;500;600&family=Roboto:wght@400;700;900&display=swap">
<style>
  :root {
    --stage: #d9dcdf;
    --card-light: #eef1f4;
    --card-light-2: #dfe4ea;
    --ink-dark: #3a3f46;
    --brand-blue: #2f5f8f;
    --panel-top: #24578a;
    --panel-bottom: #10314f;
    --divider-dark: #1b2631;
    --divider-light: #d8c9a8;
    --panel-text: #e8e2d2;
    --panel-text-soft: #d4d9df;
  }
  * { margin: 0; padding: 0; box-sizing: border-box; }
  html, body { width: 1200px; height: 969px; overflow: hidden; }
  body { background: var(--stage); position: relative; }

  .card {
    position: absolute; left: 100px; top: 199px;
    width: 1000px; height: 571px;
    border-radius: 26px; overflow: hidden;
    background: linear-gradient(160deg, var(--card-light) 0%, var(--card-light-2) 100%);
    box-shadow: 0 12px 40px rgba(0,0,0,.18);
  }
  .card-shapes { position: absolute; inset: 0; }

  .brand {
    position: absolute; left: 54px; top: 80px;
    display: flex; align-items: center; gap: 14px;
  }
  .brand-mark { width: 38px; height: 38px; background: var(--brand-blue); }
  .brand-name {
    font-family: "Roboto", sans-serif; font-weight: 900;
    font-size: 30px; line-height: 1; color: var(--brand-blue);
    letter-spacing: .5px; text-transform: uppercase;
  }

  .services {
    position: absolute; left: 49px; top: 228px;
    list-style: none;
    font-family: "Roboto", sans-serif; font-size: 19px;
    color: var(--ink-dark); text-transform: uppercase;
    line-height: 32.7px; letter-spacing: .2px;
  }

  .contact {
    position: absolute; left: 650px; top: 228px;
    font-family: "Poppins", sans-serif;
  }
  .contact-name {
    font-size: 30px; font-weight: 600; letter-spacing: .8px;
    color: var(--panel-text); line-height: 1.2;
  }
  .contact-role {
    font-size: 20px; font-weight: 500; color: var(--panel-text-soft);
    margin-top: 2px;
  }
  .contact-address {
    font-size: 21px; color: var(--panel-text-soft);
    line-height: 28px; margin-top: 20px; font-style: normal;
  }
  .contact-lines { list-style: none; margin-top: 18px; }
  .contact-lines li {
    display: flex; align-items: center; gap: 14px;
    font-size: 21px; color: var(--panel-text-soft); line-height: 28px;
  }
  .contact-lines svg { width: 16px; height: 16px; fill: var(--panel-text-soft); flex: none; }
</style>
</head>
<body>
  <div class="card">
    <svg class="card-shapes" viewBox="0 0 1000 571" preserveAspectRatio="none">
      <defs>
        <linearGradient id="panelFill" x1="0" y1="0" x2="0.4" y2="1">
          <stop offset="0" stop-color="var(--panel-top)"/>
          <stop offset="1" stop-color="var(--panel-bottom)"/>
        </linearGradient>
      </defs>
      <polygon points="752,0 1000,0 1000,571 381,571" fill="url(#panelFill)"/>
      <line x1="740" y1="0" x2="369" y2="571" stroke="var(--divider-dark)" stroke-width="8"/>
      <line x1="749" y1="0" x2="378" y2="571" stroke="var(--divider-light)" stroke-width="3"/>
    </svg>

    <div class="brand">
      <span class="brand-mark"></span>
      <span class="brand-name">Keystone Facility Services</span>
    </div>

    <ul class="services">
      <li>Asset Gathering &amp; Tracking</li>
      <li>Vendor Screening</li>
      <li>Contracting &amp; Management</li>
      <li>Service Requirement Development</li>
      <li>Work Order Processing &amp; Management</li>
      <li>Invoice Reconciliation</li>
      <li>Vendor Payment - Reporting</li>
      <li>Capital Equipment Bids</li>
      <li>&amp; Project Management</li>
    </ul>

    <div class="contact">
      <div class="contact-name">DANIEL HARPER</div>
      <div class="contact-role">President</div>
      <address class="contact-address">1420 Birchwood Avenue<br>Juneau, Alaska 99801</address>
      <ul class="contact-lines">
        <li><svg viewBox="0 0 16 16"><path d="M3 1l3 0 1.5 3.5-2 1.5a9 9 0 0 0 4.5 4.5l1.5-2L15 10v3a2 2 0 0 1-2 2C6.5 15 1 9.5 1 3a2 2 0 0 1 2-2z"/></svg>555-214-0386</li>
        <li><svg viewBox="0 0 16 16"><path d="M4.5 0h7a1 1 0 0 1 1 1v14a1 1 0 0 1-1 1h-7a1 1 0 0 1-1-1V1a1 1 0 0 1 1-1zm.7 2v10.5h5.6V2zM8 13.4a.9.9 0 1 0 0 1.8.9.9 0 0 0 0-1.8z"/></svg>555-730-4419</li>
        <li><svg viewBox="0 0 16 16"><path d="M4 1h8v4H4zM1 6h14v6h-3v3H4v-3H1zm4 4v4h6v-4z"/></svg>555-862-1907</li>
        <li><svg viewBox="0 0 16 16"><path d="M1 3h14v10H1zm1.5 1.2L8 8.5l5.5-4.3z"/></svg>info@keystonefm.com</li>
        <li><svg viewBox="0 0 16 16"><path d="M8 1a7 7 0 1 0 0 14A7 7 0 0 0 8 1zm-1 2.5l2 1-1 2 2 1v3l-2 2-1-3-2-1V6z"/></svg>www.keystonefm.com</li>
      </ul>
    </div>
  </div>
</body>
</html>
```